Redesign for a start up airline technology. The website is trelunor.com.

I need a PowerPoint template that complements our website. I can provide our current template as a starting point.

```html
<!DOCTYPE html>
<html lang="en">
<head>
<meta charset="UTF-8">
<title>Trelunor – Title Slide</title>
<link rel="stylesheet" href="https://fonts.googleapis.com/css2?family=Montserrat:wght@400;700;800&display=swap">
<style>
  :root {
    --slide-bg: #ffffff;
    --ink: #0b0b0b;
    --brand-navy: #1f4e9c;
    --band-top: #003d86;
    --band-bottom: #0a7fc6;
    --accent-green: #8fd62b;
    --muted: #6b6b6b;
    --sky-dark: #3a3a36;
    --sky-mid: #77736a;
    --haze: #b9aa94;
    --runway: #5b4c3d;
  }
  html, body {
    margin: 0;
    padding: 0;
    width: 1200px;
    height: 675px;
    overflow: hidden;
    background: var(--slide-bg);
  }
  .slide {
    position: relative;
    width: 1200px;
    height: 675px;
    overflow: hidden;
    background: var(--slide-bg);
    font-family: "Montserrat", Arial, sans-serif;
  }
  .slide-art {
    position: absolute;
    inset: 0;
    width: 1200px;
    height: 675px;
  }
  .brand {
    position: absolute;
    left: 58px;
    top: 218px;
    display: flex;
    align-items: center;
    gap: 14px;
  }
  .brand-dot {
    width: 18px;
    height: 18px;
    border-radius: 50%;
    background: var(--brand-navy);
  }
  .brand-name {
    font-weight: 800;
    font-size: 46px;
    letter-spacing: -0.5px;
    color: var(--brand-navy);
    line-height: 1;
  }
  .slide-title {
    position: absolute;
    left: 56px;
    top: 342px;
    margin: 0;
    font-weight: 800;
    font-size: 37px;
    line-height: 50px;
    color: var(--ink);
    letter-spacing: -0.2px;
  }
  .title-rule {
    position: absolute;
    left: 56px;
    top: 577px;
    width: 137px;
    height: 3px;
    background: var(--accent-green);
  }
  .confidential {
    position: absolute;
    left: 558px;
    top: 642px;
    font-size: 10px;
    color: var(--muted);
    font-weight: 400;
  }
</style>
</head>
<body>
<div class="slide">
  <svg class="slide-art" viewBox="0 0 1200 675" xmlns="http://www.w3.org/2000/svg">
    <defs>
      <linearGradient id="bandGradient" x1="0" y1="0" x2="0" y2="1">
        <stop offset="0" stop-color="var(--band-top)"/>
        <stop offset="1" stop-color="var(--band-bottom)"/>
      </linearGradient>
      <linearGradient id="photoGradient" x1="0" y1="0" x2="0" y2="1">
        <stop offset="0" stop-color="var(--sky-dark)"/>
        <stop offset="0.4" stop-color="var(--sky-mid)"/>
        <stop offset="0.68" stop-color="var(--haze)"/>
        <stop offset="1" stop-color="var(--runway)"/>
      </linearGradient>
    </defs>
    <polygon class="accent-band" points="214,0 361,0 905,675 759,675" fill="url(#bandGradient)"/>
    <polygon class="hero-photo" role="img" aria-label="Photo of a white business jet on a runway under a cloudy dusk sky"
             points="361,0 1200,0 1200,675 905,675" fill="url(#photoGradient)"/>
  </svg>

  <div class="brand">
    <span class="brand-dot"></span>
    <span class="brand-name">Trelunor</span>
  </div>

  <h1 class="slide-title">Unlocking The Future<br>Of Airline Operations<br>And The Flying<br>Experience</h1>
  <div class="title-rule"></div>

  <div class="confidential">Confidential and Proprietary</div>
</div>
</body>
</html>
```